7 Elite Label

Design a label for 7 Elite styling gels. The logo is attached. The color is C=100, M=100, Y=0, K=0. The 16 oz. jar is also attached.

Updates

Attention all designers,

The old logo has been deleted.  I have uploaded a new logo for this project.  Can you please update your design with the NEW LOGO?
thank you,
Rob

Target Market(s)

Multicultural

Requirements
Must have
• you must used the logo attached.

text to be included on the jar:

Used by Professionals
Maximum Hold
Alcohol Free
NO FLAKING

16 oz.

As far as label size, use the jar photo, and fit the design on it.

```html
<!DOCTYPE html>
<html lang="en">
<head>
<meta charset="utf-8">
<title>7 Elite Styling Gel Label</title>
<link rel="stylesheet" href="https://fonts.googleapis.com/css2?family=Roboto:wght@400;900&display=swap">
<style>
  :root {
    --page: #ffffff;
    --label-bg: #fdf5f7;
    --navy: #2e3192;
    --red: #ef3e2e;
    --frame-blue: #1f8bc9;
    --wave-blue: #b3d8f2;
    --gel-blue: #a9d3f0;
    --ghost: #ddd7ea;
  }
  * { margin: 0; padding: 0; box-sizing: border-box; }
  html, body {
    width: 1200px; height: 1000px; overflow: hidden;
    background: var(--page);
    font-family: "Roboto", Arial, sans-serif;
  }
  .label {
    position: absolute; left: 197px; top: 213px;
    width: 824px; height: 481px;
    background: var(--label-bg);
    overflow: hidden;
  }

  /* faint brand repeats at both sides */
  .ghost-disc {
    position: absolute; border-radius: 50%;
    background: var(--ghost);
  }
  .ghost-disc.left { left: -10px; top: 55px; width: 215px; height: 215px; }
  .ghost-disc.right { left: 770px; top: 80px; width: 210px; height: 210px; }
  .ghost-name {
    position: absolute; white-space: nowrap;
    font-weight: 900; font-size: 72px; line-height: 1; letter-spacing: 8px;
    color: var(--ghost);
  }
  .ghost-name.left { right: 648px; top: 300px; }
  .ghost-name.right { left: 640px; top: 300px; }

  .pattern-field {
    position: absolute; left: 150px; top: 70px;
    width: 460px; height: 400px;
    background: radial-gradient(ellipse at center, rgba(247,217,204,0.45) 0%, rgba(247,217,204,0.2) 55%, rgba(247,217,204,0) 75%);
  }

  .frame {
    position: absolute; left: 12px; top: 18px;
    width: 801px; height: 448px;
    border: 2.5px solid var(--frame-blue);
  }

  /* ornament areas, flat fill */
  .ornament { position: absolute; background: var(--wave-blue); }
  .ornament.top-right {
    left: 483px; top: 0; width: 341px; height: 100px;
    border-bottom-left-radius: 120px 100px;
    border-bottom: 3px solid var(--frame-blue);
  }
  .ornament.bottom-left {
    left: 0; top: 190px; width: 255px; height: 291px;
    border-top-right-radius: 255px 291px;
    border-top: 3px solid var(--frame-blue);
    border-right: 3px solid var(--frame-blue);
  }
  .ornament.bottom-right {
    left: 789px; top: 419px; width: 35px; height: 62px;
    background: var(--frame-blue);
  }

  .claim { position: absolute; font-weight: 400; white-space: nowrap; line-height: 1; }
  .no-flaking { left: 55px; top: 38px; font-size: 18px; color: var(--navy); }
  .alcohol-free { left: 633px; top: 36px; font-size: 20px; color: #fff; }
  .used-by {
    left: 0; width: 842px; text-align: center; top: 110px;
    font-size: 26px; letter-spacing: 3.5px; color: var(--red);
  }

  .brand {
    position: absolute; left: 281px; top: 156px;
    width: 280px; height: 236px;
    display: flex; flex-direction: column; align-items: center; justify-content: center;
    gap: 16px;
  }
  .brand-mark { width: 140px; height: 140px; border-radius: 50%; background: var(--navy); }
  .brand-name {
    font-weight: 900; font-size: 56px; letter-spacing: 6px; line-height: 1;
    color: var(--navy);
  }

  .product-line {
    left: 208px; top: 400px; font-size: 16px; letter-spacing: 2.6px; color: var(--gel-blue);
  }
  .max-hold {
    left: 0; width: 842px; text-align: center; top: 427px;
    font-size: 22px; letter-spacing: 4px; color: var(--red);
  }
  .size { left: 694px; top: 424px; font-size: 24px; color: var(--navy); }
</style>
</head>
<body>
  <div class="label">
    <div class="ghost-disc left" aria-hidden="true"></div>
    <div class="ghost-name left" aria-hidden="true">7 ELITE</div>
    <div class="ghost-disc right" aria-hidden="true"></div>
    <div class="ghost-name right" aria-hidden="true">7 ELITE</div>

    <div class="pattern-field" role="img" aria-label="Fine peach pattern of nested rotated squares"></div>

    <div class="frame"></div>

    <div class="ornament top-right" role="img" aria-label="Flowing light blue hair-wave ornament"></div>
    <div class="ornament bottom-left" role="img" aria-label="Flowing light blue hair-wave ornament"></div>
    <div class="ornament bottom-right" role="img" aria-label="Blue chevron wave ornament"></div>

    <p class="claim no-flaking">NO FLAKING</p>
    <p class="claim alcohol-free">Alcohole free</p>
    <p class="claim used-by">USED BY PROFESSIONALS</p>

    <div class="brand">
      <div class="brand-mark"></div>
      <div class="brand-name">7 ELITE</div>
    </div>

    <p class="claim product-line">Styling Gel Styling Gel Styling Gel Styling Gel Styling Gel Styling Gel</p>
    <p class="claim max-hold">MAXIMUM HOLD</p>
    <p class="claim size">16 oz.</p>
  </div>
</body>
</html>
```